professional business card

A Clean looking business card for a money transfer company. Our company is call Velorix= Transfer + Send = Transcend (next level)
to show professionalism as well as some effects to show digital tech.

1 side to have position, name and address
2 side to have company name and show that we provide money exchange and cross-border money transfer

Target Market(s)

Remittance companies and high net worth individuals

Industry/Entity Type

Finance

Contact Information for Business Card

Name, address, email, title, services- money exchange and cross-border remittance

Requirements
Nice to have
• Digital age feel

```html
<!DOCTYPE html>
<html lang="en">
<head>
<meta charset="utf-8">
<title>Velorix Business Card</title>
<link href="https://fonts.googleapis.com/css2?family=Open+Sans:wght@400;600;700;800&display=swap" rel="stylesheet">
<style>
  :root {
    --bg: #232323;
    --cyan: #72cddc;
    --teal: #1f8c9b;
    --navy: #263340;
    --white: #ffffff;
  }
  * { margin: 0; padding: 0; box-sizing: border-box; }
  html, body { width: 1200px; height: 780px; overflow: hidden; background: var(--bg); }
  body { position: relative; font-family: "Open Sans", sans-serif; }

  .card {
    position: absolute;
    top: 235px;
    width: 540px;
    height: 310px;
    border-radius: 18px;
    overflow: hidden;
  }

  /* Front: brand side */
  .card-front { left: 40px; background: var(--cyan); }
  .brand {
    position: absolute;
    left: 0; right: 0; top: 112px;
    display: flex; align-items: center; justify-content: center; gap: 14px;
  }
  .brand-dot { width: 22px; height: 22px; border-radius: 50%; background: var(--teal); }
  .brand-name {
    font-weight: 800; font-size: 54px; letter-spacing: 3px;
    color: var(--teal); text-transform: uppercase; line-height: 1;
  }
  .services {
    position: absolute; left: 0; right: 0; bottom: 34px;
    display: flex; align-items: center; justify-content: center; gap: 9px;
    color: var(--white); font-size: 13px; letter-spacing: 0.4px;
  }
  .services .sep { width: 6px; height: 6px; border-radius: 50%; background: var(--white); }

  /* Back: contact side */
  .card-back { left: 620px; background: var(--navy); }
  .card-back .bands { position: absolute; inset: 0; }
  .back-brand {
    position: absolute; left: 0; width: 250px; top: 112px;
    text-align: center;
    font-weight: 800; font-size: 44px; color: var(--cyan); line-height: 1;
  }
  .divider {
    position: absolute; left: 262px; top: 78px;
    width: 1.5px; height: 140px; background: var(--white);
  }
  .contact { position: absolute; left: 282px; top: 62px; color: var(--white); }
  .person-name { font-size: 21px; font-weight: 800; line-height: 1.1; }
  .person-name .first { color: var(--cyan); }
  .person-title { font-size: 12px; font-weight: 600; margin: 3px 0 12px 14px; }
  .address { font-size: 11.5px; line-height: 1.4; margin: 0 0 12px 14px; }
  .lines { list-style: none; margin-left: 14px; font-size: 11.5px; line-height: 1.55; }
  .lines li { display: flex; align-items: center; gap: 7px; }
  .lines svg { width: 11px; height: 11px; flex: none; fill: var(--cyan); }
</style>
</head>
<body>

<section class="card card-front">
  <div class="brand">
    <span class="brand-dot"></span>
    <span class="brand-name">Velorix</span>
  </div>
  <div class="services">
    <span>SERVICES</span><span class="sep"></span>
    <span>Money exchange</span><span class="sep"></span>
    <span>Cross-border remittance</span>
  </div>
</section>

<section class="card card-back">
  <svg class="bands" viewBox="0 0 540 310" preserveAspectRatio="none" aria-hidden="true">
    <path d="M0 272 H300 Q318 272 334 262 H372 Q352 286 320 290 H0 Z" fill="var(--cyan)"/>
    <path d="M320 258 L540 214 V236 L356 268 Q340 270 320 258 Z" fill="var(--white)"/>
  </svg>

  <div class="back-brand">Velorix</div>
  <div class="divider"></div>

  <div class="contact">
    <h1 class="person-name"><span class="first">Mara</span> Oleska</h1>
    <p class="person-title">Managing Director</p>
    <p class="address">1840 Lakeline Ave. Suite<br>310 Easton, TX 75021</p>
    <ul class="lines">
      <li>
        <svg viewBox="0 0 24 24"><path d="M6.6 10.8a15 15 0 0 0 6.6 6.6l2.2-2.2a1 1 0 0 1 1-.25 11.4 11.4 0 0 0 3.6.57 1 1 0 0 1 1 1V20a1 1 0 0 1-1 1A17 17 0 0 1 3 4a1 1 0 0 1 1-1h3.5a1 1 0 0 1 1 1c0 1.25.2 2.45.57 3.57a1 1 0 0 1-.25 1z"/></svg>
        (555) 214-0387
      </li>
      <li>
        <svg viewBox="0 0 24 24"><path d="M2 5h20v14H2z M4 7v.5l8 5 8-5V7z" fill-rule="evenodd"/></svg>
        info@velorix.com
      </li>
      <li>
        <svg viewBox="0 0 24 24"><path d="M12 2a10 10 0 1 0 0 20 10 10 0 0 0 0-20zm0 2c1.3 1.6 2.1 3.6 2.3 6H9.7C9.9 7.6 10.7 5.6 12 4zm-4.3 6H4.2a8 8 0 0 1 4.5-5.4A12 12 0 0 0 7.7 10zm0 4c.1 2 .5 3.8 1 5.4A8 8 0 0 1 4.2 14zm2 0h4.6c-.2 2.4-1 4.4-2.3 6-1.3-1.6-2.1-3.6-2.3-6zm6.6 0h3.5a8 8 0 0 1-4.5 5.4c.5-1.6.9-3.4 1-5.4zm0-4c-.1-2-.5-3.8-1-5.4a8 8 0 0 1 4.5 5.4z"/></svg>
        www.velorix.com
      </li>
    </ul>
  </div>
</section>

</body>
</html>
```